Financial Service Company Need Business Card Design

This is a new startup company, first of its kind to offer this service. We facilitate the movement of deposit funds electronically between home buyers and real estate brokerages.Our customers are DOMIVANS®, real estate brokerages, and home buyers, we identify ourselves as a financial/technology company.
Not looking for anything too flashy. Just a clean design that shows the logo, contact info, etc. Company colors can be seen on attached logo, and 'coming soon page'
www.quorvanta.ca

```html
<!DOCTYPE html>
<html lang="en">
<head>
<meta charset="utf-8">
<title>Quorvanta Business Card</title>
<link rel="stylesheet" href="https://fonts.googleapis.com/css2?family=Arimo:wght@400;700&family=Tinos&display=swap">
<style>
  :root {
    --page: #e9e6e1;
    --card: #ffffff;
    --ink: #5d5e62;
    --ink-soft: #6f7074;
    --accent: #ee5a2c;
    --rule: #f08a66;
  }
  * { box-sizing: border-box; margin: 0; padding: 0; }
  html, body { width: 1200px; height: 1000px; overflow: hidden; }
  body {
    background: var(--page);
    font-family: "Arimo", Arial, sans-serif;
    color: var(--ink);
    position: relative;
  }
  .card {
    position: absolute;
    left: 250px;
    width: 700px;
    height: 400px;
    background: var(--card);
    box-shadow: 0 6px 18px rgba(0,0,0,0.12);
  }
  /* Back of card */
  .card-back { top: 96px; }
  .card-back .brand {
    position: absolute;
    left: 0; right: 0; top: 118px;
    text-align: center;
  }
  .card-back .brand-mark {
    display: block;
    width: 74px; height: 74px;
    margin: 0 auto 22px;
    background: var(--accent);
  }
  .card-back .brand-name {
    font-size: 72px;
    font-weight: 700;
    color: var(--ink);
    letter-spacing: -1px;
    line-height: 1;
  }
  .card-back .website {
    margin-top: 18px;
    font-size: 15px;
    letter-spacing: 6px;
    color: var(--ink-soft);
  }
  /* Front of card */
  .card-front { top: 520px; padding: 46px 56px; }
  .card-front .brand {
    display: flex;
    align-items: center;
    gap: 16px;
  }
  .card-front .brand-mark {
    width: 44px; height: 44px;
    background: var(--accent);
  }
  .card-front .brand-name {
    font-size: 40px;
    font-weight: 700;
    color: var(--ink);
    letter-spacing: -0.5px;
  }
  .rule { height: 1px; background: var(--rule); }
  .rule-top { margin-top: 26px; }
  .details {
    display: flex;
    justify-content: space-between;
    margin-top: 32px;
  }
  .person-name { font-size: 24px; font-weight: 700; color: var(--ink); }
  .person-name .first { color: var(--accent); }
  .person-role {
    margin-top: 6px;
    font-size: 15px;
    letter-spacing: 5px;
    color: var(--ink);
  }
  .rule-mid { margin-top: 14px; width: 380px; }
  .label {
    font-size: 17px;
    font-weight: 700;
    color: var(--accent);
  }
  .value { font-size: 17px; color: var(--ink-soft); margin-bottom: 8px; }
  .value.phone { font-family: "Tinos", "Times New Roman", serif; font-size: 20px; }
  .contact { margin-top: 14px; }
  .address { width: 200px; }
  .address .value { line-height: 1.35; }
</style>
</head>
<body>
  <section class="card card-back" aria-label="Card back">
    <div class="brand">
      <span class="brand-mark"></span>
      <div class="brand-name">Quorvanta</div>
      <div class="website">www.quorvanta.ca</div>
    </div>
  </section>

  <section class="card card-front" aria-label="Card front">
    <div class="brand">
      <span class="brand-mark"></span>
      <span class="brand-name">Quorvanta</span>
    </div>
    <div class="rule rule-top"></div>
    <div class="details">
      <div class="person">
        <div class="person-name"><span class="first">Lena</span>Marsh</div>
        <div class="person-role">Designer</div>
        <div class="rule rule-mid"></div>
        <div class="contact">
          <div class="label">Mobile</div>
          <div class="value phone">0198-765-432</div>
          <div class="label">Email</div>
          <div class="value">lena@quorvanta.ca</div>
        </div>
      </div>
      <div class="address">
        <div class="label">Address</div>
        <div class="value">45 Maple Row St., US<br>london</div>
      </div>
    </div>
  </section>
</body>
</html>
```